Pelbrook Business Cards

Create new business cards with the details below.

Aaron Velst
Director

MB: +61 412 563 904
PH: 1300 417 639
Email: aaron.velst@pelbrook.com.au
Address: 27C Marlow Parade, Ashvale Park VIC 3094 Australia
Website: www.pelbrook.com.au

Target Market(s)

Other business

Industry/Entity Type

Business

Requirements
Must have
• must be clean looking

```html
<!DOCTYPE html>
<html lang="en">
<head>
<meta charset="utf-8">
<title>Pelbrook Business Cards</title>
<link rel="stylesheet" href="https://fonts.googleapis.com/css2?family=Montserrat:wght@600;700&family=Lato:wght@400;700&display=swap">
<style>
  :root {
    --stage: #e9e7e3;
    --charcoal: #2b2b2b;
    --charcoal-deep: #222222;
    --lime: #9ccb2f;
    --paper: #ffffff;
    --ink: #2a2a2a;
  }
  * { margin: 0; padding: 0; box-sizing: border-box; }
  html, body { width: 1200px; height: 1000px; overflow: hidden; }
  body { background: var(--stage); position: relative; font-family: "Lato", sans-serif; }

  .card { position: absolute; box-shadow: 0 6px 18px rgba(0,0,0,0.25); }

  .card-back {
    left: 80px; top: 80px; width: 830px; height: 480px;
    background: var(--charcoal);
  }
  .card-back .pattern-fill {
    position: absolute; inset: 0;
    background: linear-gradient(135deg, #2f2f2f, var(--charcoal-deep));
  }
  .card-back .back-brand {
    position: absolute; left: 470px; top: 160px;
    display: flex; align-items: center; gap: 12px;
  }
  .back-brand .brand-square { width: 22px; height: 22px; background: var(--lime); }
  .back-brand .brand-name {
    font-family: "Montserrat", sans-serif; font-weight: 700;
    font-size: 34px; color: var(--paper); letter-spacing: 1px;
  }

  .card-front {
    left: 180px; top: 420px; width: 800px; height: 440px;
    background: var(--paper); overflow: hidden;
  }
  .front-brand {
    position: absolute; left: 48px; top: 52px;
    display: flex; align-items: center; gap: 18px;
  }
  .front-brand .brand-square { width: 62px; height: 62px; background: var(--lime); }
  .front-brand .brand-name {
    font-family: "Montserrat", sans-serif; font-weight: 700;
    font-size: 58px; color: var(--ink); letter-spacing: 1px; line-height: 1;
  }

  .person { position: absolute; left: 50px; top: 184px; }
  .person-name {
    font-family: "Lato", sans-serif; font-weight: 700;
    font-size: 25px; color: var(--lime); letter-spacing: 0.5px;
  }
  .person-role { font-size: 19px; color: var(--ink); margin-top: 2px; }

  .contact-list { position: absolute; left: 50px; top: 272px; list-style: none; }
  .contact-list li {
    display: flex; align-items: center; gap: 10px;
    font-size: 20px; color: var(--ink); height: 29px;
  }
  .contact-list svg { width: 16px; height: 16px; flex: none; fill: var(--lime); }

  .stripe-motif {
    position: absolute; right: 0; top: 140px; width: 110px; height: 160px;
    background: linear-gradient(135deg, var(--charcoal) 0 45%, var(--lime) 45% 100%);
    clip-path: polygon(100% 0, 100% 100%, 0 55%);
  }

  .base-band { position: absolute; left: 0; right: 0; bottom: 0; height: 16px; }
  .base-band .band-dark {
    position: absolute; left: 0; bottom: 0; height: 16px; width: 500px;
    background: var(--charcoal);
  }
  .base-band .band-lime {
    position: absolute; right: 0; bottom: 0; height: 16px; width: 310px;
    background: var(--lime); clip-path: polygon(14px 0, 100% 0, 100% 100%, 0 100%);
  }
</style>
</head>
<body>

<section class="card card-back">
  <div class="pattern-fill" role="img" aria-label="Repeating shutter-slat pattern in dark charcoal tones"></div>
  <div class="back-brand">
    <span class="brand-square"></span>
    <span class="brand-name">PELBROOK</span>
  </div>
</section>

<section class="card card-front">
  <div class="front-brand">
    <span class="brand-square"></span>
    <span class="brand-name">PELBROOK</span>
  </div>

  <div class="person">
    <p class="person-name">AARON VELST</p>
    <p class="person-role">Director</p>
  </div>

  <ul class="contact-list">
    <li>
      <svg viewBox="0 0 16 16"><path d="M4 0h8a1 1 0 0 1 1 1v14a1 1 0 0 1-1 1H4a1 1 0 0 1-1-1V1a1 1 0 0 1 1-1zm1 2v10h6V2zm3 11a1 1 0 1 0 0 2 1 1 0 0 0 0-2z"/></svg>
      +61 412 563 904
    </li>
    <li>
      <svg viewBox="0 0 16 16"><path d="M3.6 1.2l2.3 2.6-1.2 1.8a9 9 0 0 0 5.7 5.7l1.8-1.2 2.6 2.3-1.4 2.2C8.4 14.4 1.6 7.6 1.4 2.6z"/></svg>
      1300 417 639
    </li>
    <li>
      <svg viewBox="0 0 16 16"><path d="M1 3h14v1.2L8 9 1 4.2zm0 2.6l7 4.8 7-4.8V13H1z"/></svg>
      aaron.velst@pelbrook.com.au
    </li>
    <li>
      <svg viewBox="0 0 16 16"><path d="M8 0a5.5 5.5 0 0 1 5.5 5.5C13.5 10 8 16 8 16S2.5 10 2.5 5.5A5.5 5.5 0 0 1 8 0zm0 3.3a2.2 2.2 0 1 0 0 4.4 2.2 2.2 0 0 0 0-4.4z"/></svg>
      27C Marlow Parade, Ashvale Park VIC 3094, Australia
    </li>
    <li>
      <svg viewBox="0 0 16 16"><path d="M8 0a8 8 0 1 0 0 16A8 8 0 0 0 8 0zm0 1.5c.9 0 2 1.8 2.3 5H5.7C6 3.3 7.1 1.5 8 1.5zM5.7 8h4.6c-.3 3.2-1.4 5-2.3 5S6 11.2 5.7 8zM1.6 6.5a6.5 6.5 0 0 1 3.5-4.3c-.6 1.1-.9 2.6-1 4.3zm0 1.5h2.5c.1 1.7.4 3.2 1 4.3A6.5 6.5 0 0 1 1.6 8zm10.3 0h2.5a6.5 6.5 0 0 1-3.5 4.3c.6-1.1.9-2.6 1-4.3zm0-1.5c-.1-1.7-.4-3.2-1-4.3a6.5 6.5 0 0 1 3.5 4.3z"/></svg>
      www.pelbrook.com.au
    </li>
  </ul>

  <div class="stripe-motif" role="img" aria-label="Angled charcoal and lime slat motif at the card edge"></div>

  <div class="base-band">
    <span class="band-dark"></span>
    <span class="band-lime"></span>
  </div>
</section>

</body>
</html>
```